Business Card Design

Rubber roller servicing company. Specializing in rubber to metal bonding. Serving various industries including, pharmaceutical, textile, plastic extrusion, polythene bag converting, laminating and the food industries.

Industry/Entity Type

Plastic

Contact Information for Business Card

Harwick Cylinder & Polymer Co Ltd, Desmond Pallister, Managing Director, Unit at Fernholm, Kestrel Lane, Oakbrewe, Huddersfield, West Yorkshire, HX9 2TZ, Tel 01632 960418, Fax 01632 960773, email info@harwickcylinder.co.uk,

```html
<!DOCTYPE html>
<html lang="en">
<head>
<meta charset="utf-8">
<title>Harwick Cylinder &amp; Polymer Co Ltd — Business Cards</title>
<link href="https://fonts.googleapis.com/css2?family=Questrial&family=Roboto:wght@400&display=swap" rel="stylesheet">
<style>
  :root {
    --backdrop: #bfc0c2;
    --paper: #ffffff;
    --rule-grey: #c4c4c4;
    --text-grey: #5a5a5a;
    --name-dark: #4a4a4a;
    --pink: #ec1651;
    --green: #00a54f;
  }
  * { margin: 0; padding: 0; box-sizing: border-box; }
  html, body { width: 904px; height: 1200px; overflow: hidden; }
  body { background: var(--backdrop); position: relative; font-family: "Roboto", Arial, sans-serif; }

  .card {
    position: absolute; left: 63px; width: 804px; height: 528px;
    background: var(--paper); --accent: var(--pink);
  }
  .card--pink { top: 59px; }
  .card--green { top: 609px; --accent: var(--green); }

  .contact-list { position: absolute; left: 64px; top: 52px; list-style: none; }
  .contact-list li {
    display: flex; align-items: center; height: 31px;
    font-size: 18.5px; color: var(--text-grey); letter-spacing: 0.3px;
  }
  .contact-list svg { width: 17px; height: 17px; margin-right: 12px; fill: var(--accent); }

  .person { position: absolute; left: 516px; top: 81px; }
  .person-name { font-family: "Questrial", sans-serif; font-size: 21px; color: var(--name-dark); letter-spacing: -0.3px; }
  .person-name .first { color: var(--accent); }
  .person-title { font-size: 17px; color: var(--text-grey); margin-top: 9px; }

  .divider { position: absolute; top: 153px; left: 0; height: 6px; width: 100%; display: flex; }
  .divider-grey { flex: 0 0 516px; background: var(--rule-grey); }
  .divider-accent { flex: 1; background: var(--accent); }

  .company { position: absolute; left: 62px; top: 234px; }
  .company-name {
    font-family: "Questrial", sans-serif; font-size: 34px; color: var(--accent);
    letter-spacing: -1.2px; white-space: nowrap; line-height: 1;
  }
  .company-address {
    margin-top: 22px; font-size: 18.5px; line-height: 24px;
    color: var(--text-grey); letter-spacing: 0.8px;
  }

  .footer-band { position: absolute; left: 0; bottom: 0; width: 100%; height: 111px; background: var(--accent); }
</style>
</head>
<body>

<svg width="0" height="0" style="position:absolute">
  <defs>
    <symbol id="icon-phone" viewBox="0 0 24 24"><path d="M6.6 10.8a15.1 15.1 0 0 0 6.6 6.6l2.2-2.2a1 1 0 0 1 1-.25 11.4 11.4 0 0 0 3.6.57 1 1 0 0 1 1 1V20a1 1 0 0 1-1 1A17 17 0 0 1 3 4a1 1 0 0 1 1-1h3.5a1 1 0 0 1 1 1c0 1.25.2 2.45.57 3.57a1 1 0 0 1-.25 1z"/></symbol>
    <symbol id="icon-fax" viewBox="0 0 24 24"><path d="M3 6c2-2 5-3 9-3s7 1 9 3v3h-5V7.5c-1.2-.4-2.6-.5-4-.5s-2.8.1-4 .5V9H3z"/><path d="M5 11h14l2 9H3zm4 2v2h2v-2zm4 0v2h2v-2zm-4 3v2h2v-2zm4 0v2h2v-2z"/></symbol>
    <symbol id="icon-mail" viewBox="0 0 24 24"><path d="M2 5h20v14H2zm2 2v.4l8 5.6 8-5.6V7zm0 2.8V17h16V9.8l-8 5.6z"/></symbol>
  </defs>
</svg>

<section class="card card--pink">
  <ul class="contact-list">
    <li><svg><use href="#icon-phone"/></svg>01632 960418</li>
    <li><svg><use href="#icon-fax"/></svg>01632 960773</li>
    <li><svg><use href="#icon-mail"/></svg>info@harwickcylinder.co.uk</li>
  </ul>
  <div class="person">
    <p class="person-name"><span class="first">DESMOND</span> PALLISTER</p>
    <p class="person-title">Managing Director</p>
  </div>
  <div class="divider"><span class="divider-grey"></span><span class="divider-accent"></span></div>
  <div class="company">
    <h1 class="company-name">HARWICK CYLINDER &amp; POLYMER CO LTD</h1>
    <p class="company-address">Unit at Fernholm, Kestrel Lane,<br>Oakbrewe, Huddersfield,<br>West Yorkshire, HX9 2TZ</p>
  </div>
  <div class="footer-band"></div>
</section>

<section class="card card--green">
  <ul class="contact-list">
    <li><svg><use href="#icon-phone"/></svg>01632 960418</li>
    <li><svg><use href="#icon-fax"/></svg>01632 960773</li>
    <li><svg><use href="#icon-mail"/></svg>info@harwickcylinder.co.uk</li>
  </ul>
  <div class="person">
    <p class="person-name"><span class="first">DESMOND</span> PALLISTER</p>
    <p class="person-title">Managing Director</p>
  </div>
  <div class="divider"><span class="divider-grey"></span><span class="divider-accent"></span></div>
  <div class="company">
    <h1 class="company-name">HARWICK CYLINDER &amp; POLYMER CO LTD</h1>
    <p class="company-address">Unit at Fernholm, Kestrel Lane,<br>Oakbrewe, Huddersfield,<br>West Yorkshire, HX9 2TZ</p>
  </div>
  <div class="footer-band"></div>
</section>

</body>
</html>
```